International Heavy Earthmoving Freight forwarder needs a flyer design

We need a flyer design to send out on Linkedin, Facebook, e-mail blasts, instagram etc.
We would like to announce that we have just secured a new contract offering exceptionally low shipping rates from East Coast and Gulf USA to Indonesia, Malaysia, Thailand amongst other South East Asian countries.
I would like to make it an announcement like "Hot off the press"
You can visit our instagram page for photos @bravolane
I would like the contact person on the flyer to be:
Owen Tarrel
owen.tarrel@bravolane.example
+1 555 014 2268
www.bravolane.example

Target Market(s)

Import and export used machinery equioment dealers. Mining companies, earthmoving contractors, freight forwarders

Font styles to use
Sans Serif

Requirements
Must have
• Logo, contact details, some photos from various Bravolane media outlets

```html
<!DOCTYPE html>
<html lang="en">
<head>
<meta charset="utf-8">
<title>Bravolane – International Freight for Heavy Machinery</title>
<link rel="stylesheet" href="https://fonts.googleapis.com/css2?family=Roboto:wght@400;700;900&family=Roboto+Condensed:wght@700&display=swap">
<style>
  :root {
    --brand-red: #ec1c24;
    --charcoal: #4b4b4d;
    --paper: #f2f2f3;
    --page-bg: #efefef;
    --white: #ffffff;
    --ink: #333333;
    --frame-grey: #c9c9cb;
    --sea-deep: #1c6f9e;
    --sea-light: #4fa3c9;
  }
  * { margin: 0; padding: 0; box-sizing: border-box; }
  html, body { width: 1200px; height: 1000px; overflow: hidden; background: var(--page-bg); }
  .canvas { position: relative; width: 1200px; height: 1000px; }
  .flyer {
    position: absolute; left: 130px; top: 29px;
    width: 627px; height: 628px;
    transform: scale(1.5); transform-origin: 0 0;
    background: var(--charcoal);
    overflow: hidden;
    font-family: "Roboto", Arial, sans-serif;
  }
  .red-band { position: absolute; left: 0; top: 315px; width: 627px; height: 257px; background: var(--brand-red); }
  .footer-strip { position: absolute; left: 0; top: 572px; width: 627px; height: 56px; background: var(--paper); }
  .hero-photo { position: absolute; left: 0; top: 0; width: 627px; height: 628px; }
  .announcement-tag {
    position: absolute; left: 73px; top: 0; width: 130px; height: 185px;
    background: var(--brand-red); color: var(--white);
    font-family: "Roboto Condensed", "Arial Narrow", sans-serif; font-weight: 700;
    padding: 50px 0 0 19px;
  }
  .announcement-tag .big { display: block; font-size: 46px; line-height: 40px; letter-spacing: -0.5px; }
  .announcement-tag .small {
    display: inline-block; margin-top: 6px; font-size: 19px; line-height: 18px;
    border-top: 1.5px solid var(--white); border-bottom: 1.5px solid var(--white);
    padding: 0 1px 2px;
  }
  .headline {
    position: absolute; left: 229px; top: 54px;
    color: var(--white); font-weight: 700; font-size: 27px; line-height: 34px;
  }
  .offer {
    position: absolute; left: 62px; top: 487px; width: 520px;
    color: var(--white); font-weight: 700; font-size: 12.6px; line-height: 16px;
  }
  .brand-box {
    position: absolute; left: 62px; top: 533px; width: 82px; height: 78px;
    background: var(--paper); border: 4px solid var(--frame-grey);
    display: flex; flex-direction: column; align-items: center; justify-content: center; gap: 5px;
  }
  .brand-box .brand-square { width: 22px; height: 22px; background: var(--brand-red); }
  .brand-box .brand-name { font-size: 10px; font-weight: 700; color: var(--ink); }
  .contact {
    position: absolute; left: 158px; top: 582px;
    font-size: 6.3px; line-height: 8px; color: var(--ink);
  }
</style>
</head>
<body>
<div class="canvas">
  <section class="flyer">
    <div class="red-band"></div>
    <div class="footer-strip"></div>

    <svg class="hero-photo" viewBox="0 0 627 628" role="img" aria-label="Photo of a loaded container ship sailing on open blue sea">
      <defs>
        <linearGradient id="sea" x1="0" y1="0" x2="1" y2="1">
          <stop offset="0" stop-color="var(--sea-light)"/>
          <stop offset="1" stop-color="var(--sea-deep)"/>
        </linearGradient>
      </defs>
      <path d="M0 150 H409 A163.5 163.5 0 0 1 409 477 H0 Z" fill="url(#sea)"/>
    </svg>

    <div class="announcement-tag">
      <span class="big">HOT</span>
      <span class="big">OFF</span>
      <span class="small">the press</span>
    </div>

    <h1 class="headline">International Freight<br>for Heavy Machinery</h1>

    <p class="offer">Offering exceptionally low shipping rates from East Coast and Gulf USA to Indonesia, Malaysia, Thailand amongst other South East Asian countries.</p>

    <div class="brand-box">
      <span class="brand-square"></span>
      <span class="brand-name">Bravolane</span>
    </div>

    <address class="contact" style="font-style:normal">
      Contact: Owen Tarrel, Tel: +1 555 014 2268<br>
      Email: owen.tarrel@bravolane.example<br>
      www.bravolane.example
    </address>
  </section>
</div>
</body>
</html>
```